Cloud backup company needs a new website

We need a new design for our website as the current one is quite dated now. You can view the current website at www.vaultmere-store.net.au to view the content elements.

We provide cloud backup services (ie remote off site to a cluster of servers) to small to medium businesses looking for better alternatives to tape or optical media backups.

Target Market(s)

SME/SMB (Businesses with fewer than 100 employees)

Industry/Entity Type

It Company

Requirements
Must have
• Must have sections to sign up to newsletter, log in to account, view news feed as per current website.

Must have a prominent call to action to sign up for a trial and view pricing.

Also like it to have twitter and facebook links/likes integration
Should not have
• No Flash, no serif fonts

```html
<!DOCTYPE html>
<html lang="en">
<head>
<meta charset="utf-8">
<title>vaultmere – Offsite Backup</title>
<link rel="stylesheet" href="https://fonts.googleapis.com/css2?family=Ubuntu:wght@400;500;700&family=Arimo:wght@400;700&display=swap">
<style>
:root{
  --orange:#f08a1c;
  --orange-deep:#e9720f;
  --orange-light:#f6a23a;
  --ink:#222;
  --text:#333;
  --muted:#777;
  --dark:#1e1e1e;
  --footer:#3a3a3a;
  --paper:#fff;
  --cream:#f6f3f0;
  --rule:#ddd;
}
*{box-sizing:border-box;margin:0;padding:0}
html,body{width:870px;height:1200px;overflow:hidden}
body{position:relative;background:var(--paper);font-family:"Arimo",Arial,sans-serif;color:var(--text)}
.abs{position:absolute}
.topbar{left:0;top:0;width:870px;height:6px;background:var(--footer)}
.header{left:0;top:6px;width:870px;height:109px;background:linear-gradient(#fff,#ececec)}
.brand{left:82px;top:36px;font-family:"Ubuntu",sans-serif;font-size:30px;font-weight:500;color:var(--orange);letter-spacing:.5px}
.field{height:20px;border-radius:10px;background:#e9e9e9;border:1px solid #d8d8d8;font-size:9px;color:#888;padding:4px 8px}
.login-btn{left:716px;top:30px;width:66px;height:21px;border-radius:11px;background:var(--orange);color:#fff;font:700 10px "Arimo",sans-serif;text-align:center;line-height:21px}
.acct{top:65px;font-size:9px;color:var(--orange)}
.acct.remember{color:#777}
.check{left:480px;top:67px;width:7px;height:7px;border:1px solid #ccc;background:#eee}
.nav{left:87px;top:98px;width:696px;height:33px;background:linear-gradient(#2c2c2c,#111);display:flex;border-radius:2px;z-index:2}
.nav span{color:#fff;font:500 11.5px "Ubuntu",sans-serif;line-height:33px;text-align:center;border-right:1px solid #3c3c3c}
.nav span:last-child{border-right:0}
.hero{left:0;top:115px;width:870px;height:306px;background:radial-gradient(ellipse at 60% 40%,var(--orange-light),var(--orange-deep) 75%)}
.hero-art{left:82px;top:165px;width:394px;height:210px;border-radius:6px;background:linear-gradient(135deg,#4a4a4a,#e8e8e8 45%,#3a3a3a)}
.hero-title{left:496px;top:178px;font:400 34px "Ubuntu",sans-serif;color:#fff;letter-spacing:1px}
.hero-copy{left:496px;top:228px;width:287px;font:400 11.2px/15.3px "Ubuntu",sans-serif;color:#fff;text-align:justify}
.cta{left:525px;top:334px;width:181px;height:32px;border-radius:16px;background:#fff;box-shadow:0 2px 4px rgba(0,0,0,.2);display:flex;align-items:center;gap:7px;padding-left:9px;font:700 12px "Ubuntu",sans-serif;color:var(--orange);white-space:nowrap}
.cta i{width:17px;height:17px;border-radius:50%;background:var(--orange);display:inline-block;position:relative;flex:none}
.cta i:after{content:"";position:absolute;left:4px;top:5px;width:5px;height:5px;border-right:2px solid #fff;border-top:2px solid #fff;transform:rotate(45deg)}
.dot{top:402px;width:9px;height:9px;border-radius:50%;background:#f5b060}
.dot.on{background:#222}
.how{left:0;top:421px;width:870px;height:245px;background:var(--cream)}
.how-title{left:0;top:433px;width:870px;text-align:center;font:500 18px "Ubuntu",sans-serif;color:var(--orange-deep)}
.icon-ph{width:70px;height:75px;border-radius:10px;background:linear-gradient(#cfcfcf,#8a8a8a)}
.step{top:570px;width:160px}
.step h3{text-align:center;font:400 13px "Ubuntu",sans-serif;color:#222;margin-bottom:15px}
.step p{font-size:8.8px;line-height:11.7px;text-align:justify}
.vrule{top:572px;width:1px;height:85px;background:var(--rule)}
.hrule{height:1px;background:#ccc}
.col h2{font:500 15px "Ubuntu",sans-serif;color:var(--ink);padding-bottom:10px;border-bottom:1px solid #e3e3e3;margin-bottom:10px}
.col p{font-size:8.6px;line-height:11.6px;text-align:justify;margin-bottom:11px}
.more{display:block;border-top:1px dotted #ccc;border-bottom:1px dotted #ccc;padding:6px 0;font:700 8.5px "Arimo",sans-serif;color:var(--orange-deep)}
.video{left:87px;top:717px;width:217px;height:160px;background:linear-gradient(#e8eef4,#c9d3dc);border:2px solid #222}
.play{left:168px;top:765px;width:54px;height:54px;border-radius:50%;background:rgba(20,20,20,.85)}
.play:after{content:"";position:absolute;left:22px;top:16px;border-left:17px solid #fff;border-top:11px solid transparent;border-bottom:11px solid transparent}
.vbar{left:89px;top:865px;width:213px;height:10px;background:#111}
.news-item{display:flex;gap:11px;padding:9px 0;border-bottom:1px solid #e3e3e3}
.date{width:45px;height:46px;background:#111;color:#fff;text-align:center;font:500 14px/19px "Ubuntu",sans-serif;padding-top:3px;flex:none}
.news-item p{font-size:8.6px;line-height:10.5px;text-align:justify;margin:0}
.news-item b{display:block;color:var(--orange-deep);font-size:8.6px;margin-top:5px}
.newsletter{left:565px;top:906px;width:217px;height:151px;background:var(--orange)}
.newsletter h2{font:500 17px "Ubuntu",sans-serif;color:#fff;padding:8px 10px;border-bottom:1px solid #f5a650}
.nl-field{position:absolute;left:12px;width:193px;height:22px;background:#fff;border-radius:3px;font-size:8.6px;color:#444;padding:5px 6px}
.submit{position:absolute;left:74px;top:118px;width:72px;height:20px;background:linear-gradient(#fbb733,#f39a1a);border:1px solid #e8901a;border-radius:3px;color:#fff;font:700 10px/18px "Ubuntu",sans-serif;text-align:center}
.signup{left:565px;top:1065px;width:217px;height:58px;background:var(--orange);display:flex;align-items:center;gap:10px;padding-left:10px}
.signup .sq{width:30px;height:36px;background:#fbe7cd;flex:none}
.signup div{color:#fff;font:700 24px/22px "Ubuntu",sans-serif}
.signup small{display:block;font:500 12px/15px "Ubuntu",sans-serif}
.footer{left:0;top:1148px;width:870px;height:52px;background:var(--footer);color:#fff}
.footer .links{position:absolute;left:87px;top:10px;font-size:8.8px}
.footer .copy{position:absolute;left:87px;top:32px;font-size:8.8px}
.social{top:1163px;width:24px;height:24px;border-radius:50%;background:#8a8a8a}
</style>
</head>
<body>
<div class="abs topbar"></div>
<div class="abs header"></div>
<div class="abs brand">vaultmere</div>
<div class="abs field" style="left:468px;top:31px;width:116px">User Name</div>
<div class="abs field" style="left:592px;top:31px;width:116px">Password</div>
<div class="abs login-btn">LOGIN</div>
<div class="abs check"></div>
<div class="abs acct remember" style="left:496px">Remember Me</div>
<div class="abs acct" style="left:578px">Create new account</div>
<div class="abs acct" style="left:686px">Request new password</div>

<nav class="abs nav">
  <span style="width:80px">HOME</span><span style="width:108px">SOLUTIONS</span><span style="width:99px">SERVICES</span><span style="width:97px">SUPPORT</span><span style="width:106px">PARTNERS</span><span style="width:85px">ABOUT</span><span style="width:121px">DOWNLOAD</span>
</nav>

<section class="abs hero"></section>
<div class="abs hero-art" role="img" aria-label="Laptop and tablet showing the backup software dashboard"></div>
<h1 class="abs hero-title">CLEAR DATA</h1>
<p class="abs hero-copy">Offsite Backup should be the key driver in any business continuity plan, but it doesn’t have to come with a price tag suitable only for large conglomerates. When you work with a proven provider like vaultmere, you can leverage value instead of price.</p>
<div class="abs cta"><i></i>DOWNLOAD TRAIL NOW</div>
<span class="abs dot on" style="left:416px"></span>
<span class="abs dot" style="left:431px"></span>
<span class="abs dot" style="left:446px"></span>

<section class="abs how"></section>
<h2 class="abs how-title">HOW VAULTMERE WORKS</h2>
<svg class="abs" style="left:190px;top:475px" width="500" height="80" viewBox="0 0 500 80">
  <path d="M8 30 Q60 -10 130 25 M150 60 Q220 100 300 25 M330 25 Q400 -15 475 30" fill="none" stroke="#e9720f" stroke-width="1" stroke-dasharray="3 3"/>
</svg>
<div class="abs icon-ph" style="left:128px;top:478px" role="img" aria-label="Database with disc icon"></div>
<div class="abs icon-ph" style="left:310px;top:472px" role="img" aria-label="Database with arrow icon"></div>
<div class="abs icon-ph" style="left:489px;top:472px" role="img" aria-label="Database with clock icon"></div>
<div class="abs icon-ph" style="left:667px;top:472px" role="img" aria-label="Database with restore icon"></div>

<div class="abs step" style="left:87px"><h3>INSTALL</h3><p>Lorem Ipsum is simply dummy text of the printing and typesetting industry. Lorem Ipsum has been the industry's standard dummy text ever since the 1500.</p></div>
<div class="abs vrule" style="left:255px"></div>
<div class="abs step" style="left:265px"><h3>CREATE BACKUP</h3><p>Lorem Ipsum is simply dummy text of the printing and typesetting industry. Lorem Ipsum has been the industry's standard dummy text ever since the 1500.</p></div>
<div class="abs vrule" style="left:434px"></div>
<div class="abs step" style="left:443px"><h3>SCHEDULE BACKUP</h3><p>Lorem Ipsum is simply dummy text of the printing and typesetting industry. Lorem Ipsum has been the industry's standard dummy text ever since the 1500.</p></div>
<div class="abs vrule" style="left:613px"></div>
<div class="abs step" style="left:622px"><h3>RESTORE</h3><p>Lorem Ipsum is simply dummy text of the printing and typesetting industry. Lorem Ipsum has been the industry's standard dummy text ever since the 1500.</p></div>

<div class="abs hrule" style="left:0;top:666px;width:870px"></div>

<div class="abs col" style="left:87px;top:678px;width:217px"><h2 style="border:0">View Our Demo</h2></div>
<div class="abs video" role="img" aria-label="Demo video of the backup software"></div>
<div class="abs play"></div>
<div class="abs vbar"></div>

<div class="abs col" style="left:326px;top:678px;width:217px">
  <h2>Our Services</h2>
  <p>vaultmere is the offsite backup solution designed for today, with the future in mind. It is an essential service for small to medium sized businesses as they seek to perform in a highly competitive world where uninterrupted access to proprietary and public electronic data has become so very important. If you cannot afford to lose your data, we can be of service to you.</p>
  <p>vaultmere software is a network-based solution that supports backup of files from any platform, workstation or server. Whether your company is centrally located or distributed across the country or world,</p>
  <span class="more">READ MORE »</span>
</div>
<div class="abs col" style="left:566px;top:678px;width:217px">
  <h2>Solutions</h2>
  <p>Instead of sending backups to a tape drive or other media attached to your computer, our offsite backup software encrypts and compresses your data before sending files securely over the Internet to our backup server safely offsite.</p>
  <p>This process can be scheduled when your computers are not in use and is also available on-demand, depending upon your needs. As a cross-platform software solution, offsite backup from vaultmere will run on nearly any operating system.</p>
  <span class="more">READ MORE »</span>
</div>

<div class="abs hrule" style="left:0;top:900px;width:870px"></div>

<div class="abs col" style="left:87px;top:912px;width:217px">
  <h2 style="font-weight:700">Welcome!</h2>
  <p>Most companies believe their critical data is adequately protected from a catastrophic event – until something happens. Is this really how you plan to determine whether or not your business continuity management or disaster recovery plan is 100% effective?</p>
  <p>For the Small to Medium Business Enterprise (SME), any event that wipes out all information could easily be the end of that business. As a result, no business can afford to cut corners when it comes to protecting their data from any unforeseen event.</p>
  <p>Offsite Backup is a fundamental disaster recovery requirement of any sized business or any professional in</p>
</div>

<div class="abs col" style="left:326px;top:912px;width:219px">
  <h2 style="margin-bottom:0">LATEST NEWS</h2>
  <div class="news-item"><div class="date">30<br>JAN</div><p>ectetur adipisicing elit, sed do eiusmod tempor incididunt ut labore et dolore magna aliqua. Ut enim ad minim veniam,<b>Read More</b></p></div>
  <div class="news-item"><div class="date">30<br>JAN</div><p>ectetur adipisicing elit, sed do eiusmod tempor incididunt ut labore et dolore magna aliqua. Ut enim ad minim veniam,<b>Read More</b></p></div>
  <div class="news-item" style="border:0"><div class="date">30<br>JAN</div><p>ectetur adipisicing elit, sed do eiusmod tempor incididunt ut labore et dolore magna aliqua. Ut enim ad minim veniam,<b>Read More</b></p></div>
</div>

<div class="abs newsletter">
  <h2>Newsletter</h2>
  <div class="nl-field" style="top:45px">Enter Your Name</div>
  <div class="nl-field" style="top:80px">Enter Your Email Address</div>
  <div class="submit">SUBMIT</div>
</div>
<div class="abs signup"><span class="sq"></span><div>SIGN UP FOR<small>A TRIAL AND VIEW PRICING</small></div></div>

<footer class="abs footer">
  <div class="links">Home | Solutions | Services | Support | Partners | About | Download</div>
  <div class="copy">© 2013 vaultmere Aust .All Rights Reserved.</div>
</footer>
<span class="abs social" style="left:666px" aria-label="Social link"></span>
<span class="abs social" style="left:695px" aria-label="Social link"></span>
<span class="abs social" style="left:724px" aria-label="Social link"></span>
<span class="abs social" style="left:753px" aria-label="Social link"></span>
</body>
</html>
```